Letterhead and matching envelope design for a dental office

We need a new stationary design, letterhead and envelope #10, for a dental office in Denver area. We are called Brightfield Dental. We want a simple and minimalistic design but not a boring design. I wish to have one good point that makes it look professional. I have attached our logo. Feel free to use either one. I want the design for letterhead and envelope look like a "matching pair" but not look the same. The envelope doesn't have to be white and it will have an address window on bottom left.

Target Market(s)

everyone who visits dentist (adults)

Industry/Entity Type

Dental

Font styles to use
Other font styles liked:
• close to font on logo or something that matches well

Requirements
Must have
• professional
• simple, minimalistic
• unique point that stands out
Nice to have
• matching but not same design for letterhead and envelope
Should not have
• not look like all the other boring designs
• no flowery, distracting feats

```html
<!DOCTYPE html>
<html lang="en">
<head>
<meta charset="utf-8">
<title>Brightfield Dental — Stationery</title>
<link href="https://fonts.googleapis.com/css2?family=Cormorant+SC:wght@600&family=Lato:wght@400&display=swap" rel="stylesheet">
<style>
  :root {
    --backdrop: #a3a3a3;
    --paper: #ffffff;
    --ink: #1e1e1e;
    --brand-green: #3db54a;
    --brand-green-light: #9ad18f;
    --flap-line: #777777;
    --signature-tone: #d9d9d9;
  }
  * { margin: 0; padding: 0; box-sizing: border-box; }
  html, body {
    width: 1200px; height: 960px; overflow: hidden;
    background: var(--backdrop);
    font-family: "Lato", sans-serif;
    color: var(--ink);
  }
  .canvas { position: relative; width: 1200px; height: 960px; }

  /* Letterhead */
  .letterhead {
    position: absolute; left: 34px; top: 90px;
    width: 565px; height: 798px; background: var(--paper);
  }
  .brand-name {
    position: absolute;
    font-family: "Cormorant SC", serif; font-weight: 600;
    color: var(--brand-green); white-space: nowrap;
  }
  .letterhead .brand-name { left: 60px; top: 98px; font-size: 22px; letter-spacing: 1px; }
  .contact {
    position: absolute; left: 417px; top: 72px; height: 47px;
    border-left: 1.5px solid var(--brand-green);
    padding-left: 9px; font-size: 6.8px; line-height: 1.35;
  }
  .contact-line { display: flex; align-items: center; gap: 4px; height: 10px; }
  .contact-line svg { width: 6px; height: 6px; fill: var(--brand-green); }
  .contact-address { margin-top: 3px; }
  .letter-body {
    position: absolute; left: 62px; top: 178px; width: 452px;
    font-size: 10.2px; line-height: 20px;
  }
  .letter-body p { margin-bottom: 20px; }
  .signature {
    position: absolute; left: 60px; top: 640px; width: 140px; height: 50px;
    background: linear-gradient(90deg, var(--signature-tone), #efefef);
    border-radius: 3px;
  }
  .signoff-name { position: absolute; left: 62px; top: 696px; font-size: 10.2px; }
  .footer-bands { position: absolute; left: 0; bottom: 0; width: 565px; height: 21px; }

  /* Envelope front */
  .envelope-front {
    position: absolute; left: 639px; top: 217px;
    width: 506px; height: 231px; background: var(--paper);
  }
  .envelope-front .brand-name { left: 18px; top: 46px; font-size: 11px; letter-spacing: 0.5px; }
  .return-address {
    position: absolute; left: 18px; top: 69px;
    font-size: 5.8px; line-height: 8.5px;
  }

  /* Envelope back */
  .envelope-back {
    position: absolute; left: 641px; top: 490px;
    width: 503px; height: 230px; background: var(--paper);
  }
  .flap { position: absolute; left: 0; top: 0; width: 503px; height: 64px; }
  .flap-mark {
    position: absolute; left: 0; top: 22px; width: 503px;
    display: flex; justify-content: center; align-items: center; gap: 5px;
  }
  .flap-mark .dot { width: 6px; height: 6px; border-radius: 50%; background: var(--brand-green); }
  .flap-mark .brand-name { position: static; font-size: 9px; letter-spacing: 1.5px; }
</style>
</head>
<body>
<main class="canvas">

  <section class="letterhead" aria-label="Letterhead">
    <div class="brand-name">Brightfield Dental</div>

    <div class="contact">
      <div class="contact-line">
        <svg viewBox="0 0 10 10" aria-hidden="true"><path d="M2 0.5 L4 2.8 L3 4 Q4.5 6.2 6 7 L7.2 6 L9.5 8 L8 9.5 Q3 9 0.5 2 Z"/></svg>
        <span>00 48275130</span>
      </div>
      <div class="contact-line">
        <svg viewBox="0 0 10 10" aria-hidden="true"><path d="M0.5 2 H9.5 V8.5 H0.5 Z M1 2.5 L5 5.5 L9 2.5" stroke="#fff" stroke-width="0.8"/></svg>
        <span>info@brightfield.example</span>
      </div>
      <div class="contact-address">12/40 Harlow Street<br>Eastvale City Name 0000</div>
    </div>

    <article class="letter-body">
      <p>Lorem Ipsum is simply</p>
      <p>&nbsp;dummy text of the printing and typesetting industry. Lorem Ipsum has been the industry's standard dummy text ever since the 1500s, when an unknown printer took a galley of type and scrambled it to make a type specimen book. It has survived not only five centuries, but also the leap into electronic typesetting, remaining essentially unchanged. It was popularised in the 1960s with the release of Typeforme sheets containing Lorem Ipsum passages, and more recently with desktop publishing software like Pagecraft Studio including versions of Lorem Ipsum.</p>
      <p>It is a long established fact that a reader will be distracted by the readable content of a page when looking at its layout. The point of using Lorem Ipsum is that it has a more-or-less normal distribution of letters, as opposed to using 'Content here, content here', making it look like readable English. Many desktop publishing packages and web page editors now use.</p>
      <p>&nbsp;Contrary to popular belief, Lorem Ipsum is not simply random text. It has roots in a piece of classical Latin literature from 45 BC, making it over 2000 years old. Daniel Ashworth, a Latin professor at Fairmont Ridge College in Virginia, looked up one of the more obscure Latin words, consectetur, from a Lorem Ipsum passage, and going through the cites of the word in classical literature, discovered the undoubtable source. Lorem Ipsum comes from sections 1.10.32 and 1.10.33 of "de Finibus Bonorum et Malorum" (The Extremes of Good and Evil) by Varennius, written in 45 BC. This book</p>
      <p>Lorem Ipsum</p>
    </article>

    <div class="signature" role="img" aria-label="Handwritten signature"></div>
    <div class="signoff-name">Lorem Ipsum is a dummy</div>

    <svg class="footer-bands" viewBox="0 0 565 21" preserveAspectRatio="none" aria-hidden="true">
      <polygon points="0,0 408,0 416,21 0,21" fill="var(--brand-green-light)"/>
      <polygon points="418,0 565,0 565,21 426,21" fill="var(--brand-green)"/>
    </svg>
  </section>

  <section class="envelope-front" aria-label="Envelope front">
    <div class="brand-name">Brightfield Dental</div>
    <div class="return-address">12/40 Harlow Street Eastvale<br>City Name 0000</div>
  </section>

  <section class="envelope-back" aria-label="Envelope back">
    <svg class="flap" viewBox="0 0 503 64" aria-hidden="true">
      <path d="M1 0 C6 38 14 62 36 62 L467 62 C489 62 497 38 502 0" fill="none" stroke="var(--flap-line)" stroke-width="1"/>
    </svg>
    <div class="flap-mark">
      <span class="dot"></span>
      <span class="brand-name">Brightfield Dental</span>
    </div>
  </section>

</main>
</body>
</html>
```